Redesign Application Page for Job Position

Would like to get a redesign on our Job Application Page.
You can use corvanheights or brendolix as references.

http://www.careersatxlm.example/XLM/NCreateAccount.aspx?aga=qtrwkz4hopLM7

Target Market(s)

Professional Security Individuals

Industry/Entity Type

Security Guard

Coding

Coded - Design and coding required

Number of Pages Required

1 page

Font styles to use
Sans Serif

Colors
0255a3
3276b5
ffcf3e
fee18a

Requirements
Must have
• User Friendly, Easy Navigation. Must be very easy to read and understand what is required or missing.
Should not have
• Ugly or Bulky

```html
<!DOCTYPE html>
<html lang="en">
<head>
<meta charset="utf-8">
<title>Create an Application – Xenlow Marshal Services</title>
<link rel="stylesheet" href="https://fonts.googleapis.com/css2?family=Open+Sans:wght@400;600;700&family=Ubuntu:wght@500;700&display=swap">
<style>
:root{
  --brand:#0255a3;
  --brand-2:#3276b5;
  --gold:#ffcf3e;
  --gold-soft:#fee18a;
  --ink:#333;
  --ink-soft:#555;
  --line:#6f6f6f;
  --line-strong:#333;
  --required:#d0021b;
  --bg:#fff;
}
*{box-sizing:border-box;margin:0;padding:0}
html,body{width:781px;height:1200px;overflow:hidden;background:var(--bg)}
body{position:relative;font-family:"Open Sans",Arial,sans-serif;color:var(--ink)}
.abs{position:absolute}

/* header */
.brand{left:66px;top:14px;display:flex;align-items:center;gap:10px}
.brand-mark{width:46px;height:46px;border-radius:50%;background:var(--brand)}
.brand-name{font-family:"Ubuntu",Arial,sans-serif;font-weight:700;color:var(--brand);font-size:20.5px;line-height:22px;letter-spacing:.2px}
.search{left:539px;top:34px;width:179px;height:30px;border:1px solid var(--line);display:flex;align-items:center;justify-content:space-between;padding:0 12px 0 13px;font-size:8px;color:var(--ink)}

/* panel */
.panel{left:89px;top:121px;width:604px;height:940px;border:1px solid #8a8a8a}
.title{left:0;width:781px;top:147px;text-align:center;font-family:"Ubuntu",Arial,sans-serif;font-weight:700;font-size:20.5px;color:var(--brand)}
.intro{left:0;width:781px;top:185px;text-align:center;font-size:7.3px;line-height:15px;color:var(--ink-soft)}
.instructions{left:119px;top:231px;font-size:8.2px;font-weight:700;color:var(--ink)}
.instructions .star,.req{color:var(--required)}
.date-created{left:544px;top:233px;font-size:8.2px;font-weight:700}
.date-created span{font-weight:400;color:var(--ink-soft)}

.label{font-size:9.3px;font-weight:700;color:var(--ink)}
.field{height:22px;border:1px solid var(--line);font-size:7.6px;color:var(--ink-soft);display:flex;align-items:center;justify-content:space-between;padding:0 8px}
.field svg{flex:none}

/* tables */
.grid-table{position:absolute;border-collapse:separate;border-spacing:2px;font-size:7.2px;color:var(--ink)}
.grid-table td,.grid-table th{border:1px solid var(--line);text-align:left;padding:0 4px;font-weight:400}
.grid-table th{border:1.5px solid var(--line-strong);font-weight:700;font-size:8.4px}
.license{left:118px;top:572px;width:547px}
.license th{height:25px}
.license td{height:25px}
.license small{font-size:5.4px;font-weight:700}
.license .date{color:#888;display:flex;justify-content:space-between;align-items:center;height:23px;border:none;padding:0 4px}

.availability{left:120px;top:881px;width:542px;border-collapse:collapse;font-size:7.2px}
.availability td,.availability th{border:1.5px solid var(--line-strong);height:24px;text-align:center}
.availability th{font-size:8.4px;font-weight:700}
.availability .shift{text-align:left;padding-left:13px;width:151px}
.tick{display:inline-block;width:7px;height:7px;border:1px solid #555;border-radius:1px;vertical-align:middle}

/* actions */
.btn{top:1006px;width:79px;height:30px;display:flex;align-items:center;justify-content:center;font-family:"Ubuntu",Arial,sans-serif;font-weight:700;font-size:10.5px}
.btn-primary{left:301px;background:var(--brand);color:#fff}
.btn-outline{left:402px;border:2px solid var(--brand);color:var(--brand)}

.help{left:0;width:781px;top:1079px;text-align:center;color:var(--ink)}
.help h2{font-weight:400;font-size:11.5px;margin-bottom:3px}
.help p{font-size:8px;line-height:14.5px}

.footer{left:0;top:1163px;width:781px;height:37px;background:var(--brand);color:#fff;font-size:7.4px}
.footer .copy{position:absolute;left:0;width:781px;top:13px;text-align:center}
.footer .code{position:absolute;left:743px;top:15px;font-size:7.2px}
</style>
</head>
<body>

<header>
  <div class="abs brand">
    <div class="brand-mark"></div>
    <div class="brand-name">XENLOW MARSHAL<br>SERVICES, INC.</div>
  </div>
  <div class="abs search">Search
    <svg width="8" height="8" viewBox="0 0 10 10"><circle cx="4" cy="4" r="3" fill="none" stroke="#333" stroke-width="1.5"/><line x1="6.3" y1="6.3" x2="9" y2="9" stroke="#333" stroke-width="1.5"/></svg>
  </div>
</header>

<main>
  <div class="abs panel"></div>
  <h1 class="abs title">Create an Application</h1>
  <p class="abs intro">Lorem Ipsum is simply dummy text. Lorem Ipsum is simply dummy text of the printing and typesetting industry.<br>Lorem Ipsum has been the industry's standard dummy text ever since the 1500s.</p>
  <p class="abs instructions">Complete all required fields ( red star &nbsp;<span class="star">*</span>), then click "Continue" to create your account!</p>
  <p class="abs date-created">Date Created - &nbsp;<span>04 - Jan - 2018</span></p>

  <!-- Name / Email -->
  <div class="abs label" style="left:122px;top:268px">Name <span class="req">*</span></div>
  <div class="abs label" style="left:474px;top:271px">Email</div>
  <div class="abs field" style="left:120px;top:291px;width:108px">First Name</div>
  <div class="abs field" style="left:237px;top:291px;width:108px">Middle Name</div>
  <div class="abs field" style="left:354px;top:291px;width:108px">Last Name</div>
  <div class="abs field" style="left:474px;top:291px;width:190px"></div>

  <!-- Phone / DOB / Gender -->
  <div class="abs label" style="left:122px;top:341px">Phone Number</div>
  <div class="abs label" style="left:356px;top:341px">Date of Birth</div>
  <div class="abs label" style="left:517px;top:341px">Gender</div>
  <div class="abs field" style="left:120px;top:364px;width:108px">Cell</div>
  <div class="abs field" style="left:237px;top:364px;width:108px">Home</div>
  <div class="abs field" style="left:355px;top:364px;width:148px">mm / dd / yyyy
    <svg width="8" height="8" viewBox="0 0 10 10"><rect x=".5" y="1.5" width="9" height="8" fill="none" stroke="#555"/><rect x=".5" y="1.5" width="9" height="2" fill="#555"/><path d="M2 5h6M2 7h6M4 4v5M6 4v5" stroke="#555" stroke-width=".6"/></svg></div>
  <div class="abs field" style="left:516px;top:364px;width:148px">Select <svg width="6" height="4" viewBox="0 0 6 4"><path d="M.5.5 3 3 5.5.5" fill="none" stroke="#555"/></svg></div>

  <!-- Address -->
  <div class="abs label" style="left:122px;top:408px">Street Address <span class="req">*</span></div>
  <div class="abs label" style="left:267px;top:408px">City</div>
  <div class="abs label" style="left:411px;top:408px">State</div>
  <div class="abs label" style="left:556px;top:408px">Zip Code <span class="req">*</span></div>
  <div class="abs field" style="left:120px;top:431px;width:134px">Select <svg width="6" height="4" viewBox="0 0 6 4"><path d="M.5.5 3 3 5.5.5" fill="none" stroke="#555"/></svg></div>
  <div class="abs field" style="left:265px;top:431px;width:134px">Select <svg width="6" height="4" viewBox="0 0 6 4"><path d="M.5.5 3 3 5.5.5" fill="none" stroke="#555"/></svg></div>
  <div class="abs field" style="left:410px;top:431px;width:134px">Select <svg width="6" height="4" viewBox="0 0 6 4"><path d="M.5.5 3 3 5.5.5" fill="none" stroke="#555"/></svg></div>
  <div class="abs field" style="left:555px;top:431px;width:108px"></div>

  <!-- Office / Position / SSN -->
  <div class="abs label" style="left:122px;top:481px">Nearest Office</div>
  <div class="abs label" style="left:307px;top:481px">Job Position</div>
  <div class="abs label" style="left:490px;top:481px">SSN <span class="req">*</span></div>
  <div class="abs field" style="left:120px;top:503px;width:174px">Select <svg width="6" height="4" viewBox="0 0 6 4"><path d="M.5.5 3 3 5.5.5" fill="none" stroke="#555"/></svg></div>
  <div class="abs field" style="left:305px;top:503px;width:174px">Select <svg width="6" height="4" viewBox="0 0 6 4"><path d="M.5.5 3 3 5.5.5" fill="none" stroke="#555"/></svg></div>
  <div class="abs field" style="left:490px;top:503px;width:173px"></div>

  <!-- License -->
  <div class="abs label" style="left:121px;top:552px">License Details</div>
  <table class="grid-table license">
    <tr><th style="width:260px">Type</th><th style="width:140px">Number</th><th>Expire Date</th></tr>
    <tr><td>Guard Card</td><td></td><td><div class="date">mm / dd / yyyy <svg width="8" height="8" viewBox="0 0 10 10"><rect x=".5" y="1.5" width="9" height="8" fill="none" stroke="#666"/><rect x=".5" y="1.5" width="9" height="2" fill="#666"/><path d="M2 5h6M2 7h6M4 4v5M6 4v5" stroke="#666" stroke-width=".6"/></svg></div></td></tr>
    <tr><td>Baton</td><td></td><td><div class="date">mm / dd / yyyy <svg width="8" height="8" viewBox="0 0 10 10"><rect x=".5" y="1.5" width="9" height="8" fill="none" stroke="#666"/><rect x=".5" y="1.5" width="9" height="2" fill="#666"/><path d="M2 5h6M2 7h6M4 4v5M6 4v5" stroke="#666" stroke-width=".6"/></svg></div></td></tr>
    <tr><td>Gun Permit</td><td></td><td><div class="date">mm / dd / yyyy <svg width="8" height="8" viewBox="0 0 10 10"><rect x=".5" y="1.5" width="9" height="8" fill="none" stroke="#666"/><rect x=".5" y="1.5" width="9" height="2" fill="#666"/><path d="M2 5h6M2 7h6M4 4v5M6 4v5" stroke="#666" stroke-width=".6"/></svg></div></td></tr>
    <tr><td>Transportation Workers Identification Card <small>(TWIC)</small></td><td></td><td><div class="date">mm / dd / yyyy <svg width="8" height="8" viewBox="0 0 10 10"><rect x=".5" y="1.5" width="9" height="8" fill="none" stroke="#666"/><rect x=".5" y="1.5" width="9" height="2" fill="#666"/><path d="M2 5h6M2 7h6M4 4v5M6 4v5" stroke="#666" stroke-width=".6"/></svg></div></td></tr>
    <tr><td>Merchant Mariner Credential <small>(MMC)</small></td><td></td><td><div class="date">mm / dd / yyyy <svg width="8" height="8" viewBox="0 0 10 10"><rect x=".5" y="1.5" width="9" height="8" fill="none" stroke="#666"/><rect x=".5" y="1.5" width="9" height="2" fill="#666"/><path d="M2 5h6M2 7h6M4 4v5M6 4v5" stroke="#666" stroke-width=".6"/></svg></div></td></tr>
    <tr><td>Standards of Training, Certification and Watchkeeping for Seafarers <small>(SCTW)</small></td><td></td><td><div class="date">mm / dd / yyyy <svg width="8" height="8" viewBox="0 0 10 10"><rect x=".5" y="1.5" width="9" height="8" fill="none" stroke="#666"/><rect x=".5" y="1.5" width="9" height="2" fill="#666"/><path d="M2 5h6M2 7h6M4 4v5M6 4v5" stroke="#666" stroke-width=".6"/></svg></div></td></tr>
  </table>

  <!-- ID / Languages / Source -->
  <div class="abs label" style="left:121px;top:792px">ID Document Type</div>
  <div class="abs label" style="left:308px;top:792px">Additional Languages</div>
  <div class="abs label" style="left:490px;top:792px">How did you hear about us?</div>
  <div class="abs field" style="left:120px;top:814px;width:174px">Select <svg width="6" height="4" viewBox="0 0 6 4"><path d="M.5.5 3 3 5.5.5" fill="none" stroke="#555"/></svg></div>
  <div class="abs field" style="left:305px;top:814px;width:174px">Select <svg width="6" height="4" viewBox="0 0 6 4"><path d="M.5.5 3 3 5.5.5" fill="none" stroke="#555"/></svg></div>
  <div class="abs field" style="left:490px;top:814px;width:173px">Select <svg width="6" height="4" viewBox="0 0 6 4"><path d="M.5.5 3 3 5.5.5" fill="none" stroke="#555"/></svg></div>

  <!-- Work availability -->
  <div class="abs label" style="left:121px;top:859px">Work Availability</div>
  <table class="grid-table availability">
    <tr><th class="shift">Shift</th><th>Sun</th><th>Mon</th><th>Tue</th><th>Wed</th><th>Thu</th><th>Fri</th><th>Sat</th></tr>
    <tr><td class="shift">Day Shift</td><td><span class="tick"></span></td><td><span class="tick"></span></td><td><span class="tick"></span></td><td><span class="tick"></span></td><td><span class="tick"></span></td><td><span class="tick"></span></td><td><span class="tick"></span></td></tr>
    <tr><td class="shift">Swing Shift</td><td><span class="tick"></span></td><td><span class="tick"></span></td><td><span class="tick"></span></td><td><span class="tick"></span></td><td><span class="tick"></span></td><td><span class="tick"></span></td><td><span class="tick"></span></td></tr>
    <tr><td class="shift">Night Shift</td><td><span class="tick"></span></td><td><span class="tick"></span></td><td><span class="tick"></span></td><td><span class="tick"></span></td><td><span class="tick"></span></td><td><span class="tick"></span></td><td><span class="tick"></span></td></tr>
  </table>

  <div class="abs btn btn-primary">Continue</div>
  <div class="abs btn btn-outline">Discard</div>

  <section class="abs help">
    <h2>Need Help?</h2>
    <p>Call us at: (555) 014-7290<br>and ask for a Human Resource representative.</p>
  </section>
</main>

<footer class="abs footer">
  <div class="copy">© Copyright 2018. All Rights Reserved.</div>
  <div class="code">C27</div>
</footer>

</body>
</html>
```